Shop Window Signs and Fence Designs

Hi guys im looking for creativity people in helping me with these designs 50 all up

Designs on various signage displays for shop windows and store fronts.

50 separate designs with on going work available.
Each design to be suppled in PDF

20 - Vertical designs - (posters)
20 - Horizontal designs - (banners) for hanging on fences e.g.
5 - Vertical - sales, garage sale EG
5 - Horizontal - sales, garage sale EG

MIX THINGS UP GUYS these are my samples below

At this stage only looking at straight eges designs.

COLOUR FULL DESIGNS EYE CATCHING
thanks guys lots more work to come for the right designer

Target Market(s)

Customers - Shoppers

Industry/Entity Type

Shop

Font styles to use
Serif
Sans Serif
Decorative
Script

Colors

Designer to choose colors to be used in the design.

Requirements
Must have
• POSTERS - in VERTICAL format
• 1900 x 1320 200gsm
• 2600 x 1600 200gsm
• 1540 x 1060 250gsm
• 2440 x1320 200gsm
• BANNERS - in HORIZONTAL format
• 1000 x 5000
• 1000 x 4000
• 1000 x 3000
• 1000 x 2000
Nice to have
• Be creative
Should not have
• Be creative

```html
<!DOCTYPE html>
<html lang="en">
<head>
<meta charset="utf-8">
<title>Sale – Up to 50% Off Storewide</title>
<link rel="stylesheet" href="https://fonts.googleapis.com/css2?family=Bungee&family=Open+Sans:wght@400;500&family=Syncopate:wght@700&display=swap">
<style>
  :root {
    --page: #ffffff;
    --sign-cream: #fbf6bd;
    --sale-red: #ee2a33;
    --ink: #231f20;
    --wide-green: #58f500;
  }
  html, body {
    margin: 0;
    padding: 0;
    width: 1200px;
    height: 960px;
    overflow: hidden;
    background: var(--page);
  }
  .sale-sign {
    display: block;
    width: 1200px;
    height: 960px;
  }
  .sign-panel { fill: var(--sign-cream); }
  .headline-sale {
    font-family: "Syncopate", "Arial Black", sans-serif;
    font-weight: 700;
    font-size: 140px;
    fill: var(--sale-red);
  }
  .offer-upto {
    font-family: "Open Sans", Arial, sans-serif;
    font-weight: 400;
    font-size: 86px;
    fill: var(--ink);
  }
  .offer-figure {
    font-family: "Open Sans", Arial, sans-serif;
    font-weight: 500;
    font-size: 310px;
    fill: var(--sale-red);
  }
  .offer-percent {
    font-family: "Open Sans", Arial, sans-serif;
    font-weight: 400;
    font-size: 170px;
    fill: var(--ink);
  }
  .offer-off {
    font-family: "Open Sans", Arial, sans-serif;
    font-weight: 400;
    font-size: 78px;
    fill: var(--ink);
  }
  .tagline-store {
    font-family: "Open Sans", Arial, sans-serif;
    font-weight: 400;
    font-size: 128px;
    fill: var(--ink);
  }
  .tagline-wide {
    font-family: "Bungee", Impact, sans-serif;
    font-size: 230px;
    fill: var(--wide-green);
  }
</style>
</head>
<body>
<svg class="sale-sign" viewBox="0 0 1200 960" xmlns="http://www.w3.org/2000/svg" role="img" aria-label="Sale – up to 50% off storewide">
  <rect class="sign-panel" x="87" y="93" width="1016" height="768"/>

  <text class="headline-sale" x="176" y="251" textLength="883" lengthAdjust="spacing">SALE</text>

  <g class="offer">
    <text class="offer-upto" transform="translate(422 586) rotate(-90)" x="0" y="0" textLength="222" lengthAdjust="spacingAndGlyphs">UP TO</text>
    <text class="offer-figure" x="440" y="586" textLength="334" lengthAdjust="spacingAndGlyphs">50</text>
    <text class="offer-percent" x="798" y="487" textLength="137" lengthAdjust="spacingAndGlyphs">%</text>
    <text class="offer-off" x="802" y="586" textLength="144" lengthAdjust="spacingAndGlyphs">OFF</text>
  </g>

  <g class="tagline">
    <text class="tagline-store" x="131" y="784" textLength="338" lengthAdjust="spacingAndGlyphs">STORE</text>
    <text class="tagline-wide" transform="rotate(-2 780 740)" x="477" y="815" textLength="603" lengthAdjust="spacingAndGlyphs">WIDE</text>
  </g>
</svg>
</body>
</html>
```